Creating a label for germicidal disposable wipes.

I need to create a label to put on our containers of germicidal disposable wipes. I am attaching an example of another germicidal wipe that I would like a similar format but more customized to look like my companies.

```html
<!DOCTYPE html>
<html lang="en">
<head>
<meta charset="utf-8">
<title>KVR Shield Large Wipe – Label</title>
<link href="https://fonts.googleapis.com/css2?family=Oswald:wght@400;500;600;700&family=Roboto+Condensed:ital,wght@0,400;0,700;1,400&display=swap" rel="stylesheet">
<style>
  :root{
    --bg:#ececec;
    --green:#2fb24b;
    --green-deep:#1e8f3a;
    --green-light:#45c85a;
    --green-text:#3fd351;
    --navy:#2f2b80;
    --navy-deep:#26226d;
    --white:#ffffff;
    --grey:#8d8d95;
  }
  *{box-sizing:border-box;margin:0;padding:0}
  html,body{width:1200px;height:718px;overflow:hidden;background:var(--bg)}
  body{font-family:"Roboto Condensed",sans-serif;color:var(--white)}
  .label{position:absolute;left:192px;top:9px;width:816px;height:700px;background:var(--navy);box-shadow:4px 6px 14px rgba(0,0,0,.25);overflow:hidden}
  .front{position:absolute;left:0;top:0;width:540px;height:700px;
    background:linear-gradient(160deg,var(--green-light) 0%,var(--green) 45%,var(--green-deep) 100%)}
  .front-facets{position:absolute;left:0;top:169px;width:540px;height:371px}
  .header{position:absolute;left:0;top:0;width:540px;height:169px;
    background:linear-gradient(180deg,var(--green) 0%,#2a7f5e 40%,var(--navy) 100%);border-bottom-right-radius:18px}
  .brand{position:absolute;left:42px;top:36px;display:flex;align-items:center;gap:14px}
  .brand-dot{width:58px;height:58px;border-radius:50%;background:var(--green-deep)}
  .brand-name{font-family:"Oswald",sans-serif;font-weight:500;font-size:66px;line-height:1;letter-spacing:1px}
  .brand-division{position:absolute;left:142px;top:103px;font-family:"Oswald",sans-serif;font-size:15px;letter-spacing:1px;color:#1d1b55}
  .brand-tagline{position:absolute;left:48px;top:127px;font-family:"Oswald",sans-serif;font-size:16px;color:var(--green-text);letter-spacing:.5px}
  .divider{position:absolute;left:340px;top:40px;width:2px;height:100px;background:var(--white)}
  .product{position:absolute;left:362px;top:34px;width:150px;text-align:center}
  .product-name{font-family:"Oswald",sans-serif;font-weight:700;font-size:52px;line-height:1.05;border-bottom:2px solid var(--white);padding-bottom:4px}
  .product-size{font-family:"Oswald",sans-serif;font-size:18px;margin-top:8px}
  .steps{position:absolute;left:40px;top:183px;width:420px;height:110px}
  .step-link{position:absolute;top:53px;left:60px;width:300px;height:3px;background:var(--white)}
  .step{position:absolute;top:0;width:108px;height:108px;border-radius:50%;background:var(--navy);border:4px solid var(--white)}
  .step-timer{left:12px;text-align:center;font-family:"Oswald",sans-serif;line-height:1}
  .step-timer b{display:block;font-size:56px;font-weight:700;margin-top:8px}
  .step-timer span{font-size:14px}
  .step-hand{left:154px}.step-flush{left:297px}
  .step-mark{position:absolute;inset:14px;border-radius:50%;background:#4a46a0}
  .step-captions{position:absolute;top:302px;left:0;width:540px;font-family:"Oswald",sans-serif;font-size:13.5px}
  .step-captions span{position:absolute;transform:translateX(-50%);white-space:nowrap}
  .claim{position:absolute;left:52px;top:338px;font-family:"Oswald",sans-serif;font-size:17px;color:var(--navy)}
  .ingredients{position:absolute;left:52px;top:373px;width:424px;font-family:"Oswald",sans-serif}
  .ingredients h2{font-size:18px;font-weight:600;text-decoration:underline;margin-bottom:10px}
  .ingredient{display:flex;align-items:baseline;font-size:17px;height:23.5px}
  .ingredient .leader{flex:1;border-bottom:2px dotted var(--white);margin:0 4px;transform:translateY(-4px)}
  .note{font-family:"Roboto Condensed",sans-serif;font-style:italic;font-size:15px;margin-top:6px}
  .warning{position:absolute;left:0;top:540px;width:540px;height:125px;background:var(--navy)}
  .keep-out{position:absolute;left:52px;top:10px;font-family:"Oswald",sans-serif;font-size:22px;color:var(--green-text)}
  .warning-line{position:absolute;left:52px;top:36px;display:flex;align-items:center;gap:8px}
  .warning-word{font-family:"Oswald",sans-serif;font-weight:500;font-size:34px;letter-spacing:.5px}
  .warning-note{font-size:13.5px;line-height:1.1}
  .contents{position:absolute;left:52px;top:78px;font-family:"Oswald",sans-serif;font-size:20px;white-space:nowrap}
  .contents small{font-size:12px}
  .net-weight{position:absolute;left:52px;top:106px;font-size:11.5px}
  .seal{position:absolute;left:385px;top:22px;width:82px;height:82px;border-radius:50%;background:var(--grey);opacity:.55}
  .base-strip{position:absolute;left:0;top:665px;width:540px;height:35px;background:var(--green)}
  .back{position:absolute;left:540px;top:0;width:276px;height:700px;padding:34px 24px 0 26px;background:var(--navy-deep)}
  .back h3{font-family:"Oswald",sans-serif;font-weight:400;font-size:17px;margin-bottom:12px}
  .back p{font-size:10.4px;line-height:1.42;margin-bottom:12px}
  .back p strong{font-family:"Oswald",sans-serif;font-weight:400;font-size:14px}
</style>
</head>
<body>
<main class="label">
  <section class="front">
    <svg class="front-facets" viewBox="0 0 540 371" aria-hidden="true">
      <polygon points="0,0 240,0 120,371 0,371" fill="#3cc353" opacity=".45"/>
      <polygon points="300,0 540,0 540,260" fill="#1d8d3a" opacity=".45"/>
      <polygon points="380,371 540,180 540,371" fill="#53d168" opacity=".35"/>
    </svg>

    <header class="header">
      <div class="brand"><span class="brand-dot"></span><span class="brand-name">KVR</span></div>
      <div class="brand-division">HAZARDOUS DIVISION</div>
      <div class="brand-tagline">CLINICAL WASTE SYSTEMS</div>
      <span class="divider"></span>
      <div class="product">
        <div class="product-name">SHIELD</div>
        <div class="product-size">LARGE WIPE</div>
      </div>
    </header>

    <div class="steps">
      <span class="step-link"></span>
      <div class="step step-timer"><b>2</b><span>MINUTES</span></div>
      <div class="step step-hand"><span class="step-mark" role="img" aria-label="Icon: hands with a crossed-out wipe"></span></div>
      <div class="step step-flush"><span class="step-mark" role="img" aria-label="Icon: crossed-out toilet"></span></div>
    </div>
    <div class="step-captions">
      <span style="left:94px">DISINFECTS IN</span>
      <span style="left:248px">NOT A SKIN OR BABY WIPE</span>
      <span style="left:391px">DO NOT FLUSH</span>
    </div>

    <p class="claim">BACTERICIDAL, TUBERCULOCIDAL, AND VIRUCIDAL * IN 2 MINUTES</p>

    <div class="ingredients">
      <h2>ACTIVE INGREDIENTS</h2>
      <div class="ingredient"><span>BACTERICIDAL,</span><span class="leader"></span><span>05%</span></div>
      <div class="ingredient"><span>TUBERCULOCIDAL</span><span class="leader"></span><span>05%</span></div>
      <div class="ingredient"><span>VIRUCIDAL</span><span class="leader"></span><span>05%</span></div>
      <div class="ingredient"><span>BACTERICIDAL,</span><span class="leader"></span><span>05%</span></div>
      <p class="note">Does not icludie the weight of thr wipe</p>
    </div>

    <div class="warning">
      <p class="keep-out">KEEP OUT OF REACH OF CHILDREN</p>
      <div class="warning-line">
        <span class="warning-word">WARNING</span>
        <span class="warning-note">See back panel for additional<br>precautionary statements</span>
      </div>
      <p class="contents">Contains: 160 wipes <small>6x6.75in (15.2 x 17.1cm)</small></p>
      <p class="net-weight">Net Wt. 1 lb 13 oz (833g)</p>
      <span class="seal"></span>
    </div>
    <div class="base-strip"></div>
  </section>

  <aside class="back">
    <h3>Title Here:</h3>
    <p><strong>Lorem ipsum</strong> dolor sit amet, consectetuer adipiscing elit, sed diam nonummy nibh euismod tincidunt ut laoreet dolore magna aliquam erat volutpat. Ut wisi enim ad minim veniam, quis nostrud exerci tation ullamcorper suscipit lobortis nisl ut aliquip ex ea commodo consequat. Duis autem vel eum iriure dolor in hendrerit in vulputate velit esse molestie consequat, vel illum dolore eu feugiat nulla facilisis at vero eros et accumsan et iusto odio dignissim qui blandit praesent luptatum zzril delenit augue duis dolore te feugait nulla facilisi.</p>
    <p><strong>Lorem ipsum</strong> dolor sit amet, cons ectetuer adipiscing elit, sed diam nonummy nibh euismod tincidunt ut laoreet dolore magna aliquam erat volutpat. Ut wisi enim ad minim veniam, quis nostrud exerci tation ullamcorper suscipit lobortis nisl ut aliquip ex ea commodo consequat. Lorem ipsum dolor sit amet, consectetuer adipiscing elit, sed diam nonummy nibh euismod tincidunt ut laoreet dolore magna aliquam erat volutpat. Ut wisi enim ad minim veniam, quis nostrud exerci tation ullamcorper suscipit lobortis nisl ut aliquip ex ea commodo consequat. Duis autem vel eum iriure dolor in hendrerit in vulputate velit esse molestie consequat, vel illum dolore eu feugiat nulla facilisis at vero eros et accumsan et iusto odio dignissim qui blandit praesent luptatum zzril delenit augue duis dolore te feugait nulla facilisi.</p>
    <p><strong>Lorem ipsum</strong> dolor sit amet, cons ectetuer adipiscing elit, sed diam nonummy nibh euismod tincidunt ut laoreet dolore magna aliquam erat volutpat. Ut wisi enim ad minim veniam, quis nostrud exerci tation ullamcorper suscipit lobortis nisl ut aliquip ex ea commodo consequat.</p>
  </aside>
</main>
</body>
</html>
```